A small boutique Accounting and Mortgage Broking firm needs a business card design

Quorvel is a Brisbane based boutique accounting and mortgage broking firm. We offer a range of extensive financial services like accounting, tax consulting, book-keeping and mortgage broking.
We need a business card that stands out. The content can stay as it is on the existing card unless you recommend us to change anything on it for a better design.
Please remove the mobile number and give us a suitable format to change the details like email address and name.
Industry/Entity Type
Business
Contact Information for Business Card
Dalian Okoruwe
Quorvel Group Pty Ltd
3/412 Brackwin Rd Salisbury QLD 4107
PO Box 829 Salisbury QLD 4107
T 07 3184 5526
F 07 3952 1087
E dokoruwe@quorvel.net.au
Accountants Tax Agents, Mortgage Brokers
www.quorvel.net.au
Look and feel
Each slider illustrates characteristics of the customer's brand and the style your logo design should communicate.

```html
<!DOCTYPE html>
<html lang="en">
<head>
<meta charset="UTF-8">
<title>Quorvel Business Card</title>
<link rel="stylesheet" href="https://fonts.googleapis.com/css2?family=Roboto:wght@400;500;700&family=Open+Sans:wght@400&display=swap">
<style>
  :root {
    --brand-green: #7dc243;
    --brand-charcoal: #333334;
    --card-white: #ffffff;
    --backdrop: #ece6db;
    --text-dark: #2b2b2b;
  }
  * { margin: 0; padding: 0; box-sizing: border-box; }
  html, body { width: 1200px; height: 741px; overflow: hidden; }
  body {
    background: var(--backdrop);
    position: relative;
    font-family: "Roboto", Arial, sans-serif;
    color: var(--text-dark);
  }
  .card {
    position: absolute;
    border-radius: 14px;
    overflow: hidden;
    box-shadow: 0 4px 14px rgba(0,0,0,0.12);
    text-align: center;
  }
  .card-front {
    left: 129px; top: 82px; width: 320px; height: 560px;
    background: var(--card-white);
  }
  .card-back {
    left: 572px; top: 286px; width: 554px; height: 316px;
    background: var(--brand-green);
  }
  .brand-lockup {
    position: absolute; left: 0; right: 0;
    display: flex; align-items: center; justify-content: center; gap: 10px;
  }
  .brand-dot {
    border-radius: 50%;
    background: var(--brand-charcoal);
    flex: none;
  }
  .brand-name { font-weight: 700; letter-spacing: -0.5px; line-height: 1; }
  .card-front .brand-lockup { top: 76px; }
  .card-front .brand-dot { width: 54px; height: 54px; }
  .card-front .brand-name { font-size: 46px; color: var(--brand-green); }
  .card-back .brand-lockup { top: 95px; gap: 14px; }
  .card-back .brand-dot { width: 76px; height: 76px; }
  .card-back .brand-name { font-size: 64px; color: var(--card-white); }
  .tagline {
    position: absolute; left: 0; right: 0;
    font-family: "Open Sans", Arial, sans-serif;
    letter-spacing: 0.3px;
    line-height: 1;
  }
  .card-front .tagline { top: 149px; font-size: 19px; color: var(--text-dark); }
  .card-back .tagline { top: 189px; font-size: 27px; color: var(--brand-charcoal); }
  .company {
    position: absolute; left: 0; right: 0; top: 192px;
    font-size: 23px; font-weight: 500; line-height: 26px;
  }
  .person {
    position: absolute; left: 0; right: 0; top: 274px;
    font-size: 31px; font-weight: 500; line-height: 36px;
    color: var(--brand-green);
  }
  .contact-line {
    position: absolute; left: 0; right: 0;
    display: flex; align-items: center; justify-content: center; gap: 17px;
    font-size: 22px; font-weight: 500; line-height: 26px;
  }
  .contact-phone { top: 350px; }
  .contact-fax { top: 378px; }
  .contact-icon { width: 24px; height: 24px; flex: none; }
  .email {
    position: absolute; left: 0; right: 0; top: 407px;
    font-size: 16px; line-height: 20px;
  }
  .address {
    position: absolute; left: 0; right: 0; top: 438px;
    font-size: 16px; font-weight: 500; line-height: 21px;
  }
  .web-band {
    position: absolute; left: 0; right: 0; bottom: 0; height: 52px;
    background: var(--brand-charcoal);
    color: var(--brand-green);
    font-size: 25px; font-weight: 500;
    display: flex; align-items: center; justify-content: center;
  }
  .services {
    position: absolute; left: 0; right: 0; top: 233px;
    font-size: 15px; font-weight: 500; line-height: 18px;
    color: var(--card-white);
  }
  .services .sep { margin: 0 4px; }
</style>
</head>
<body>
  <section class="card card-front">
    <div class="brand-lockup">
      <span class="brand-dot"></span>
      <span class="brand-name">Quorvel</span>
    </div>
    <p class="tagline">CLEAR. SOUND. AHEAD.</p>
    <p class="company">Quorvel Group Pty Ltd</p>
    <p class="person">Dalian Okoruwe</p>
    <div class="contact-line contact-phone">
      <svg class="contact-icon" viewBox="0 0 24 24" aria-hidden="true">
        <rect width="24" height="24" rx="4" fill="#7dc243"/>
        <path d="M5 10 Q12 4 19 10 L17 12 L15 10 L9 10 L7 12 Z" fill="#fff"/>
        <rect x="7" y="12" width="10" height="7" rx="1" fill="#fff"/>
        <circle cx="12" cy="15.5" r="1.8" fill="#7dc243"/>
      </svg>
      <span>07 3184 5526</span>
    </div>
    <div class="contact-line contact-fax">
      <svg class="contact-icon" viewBox="0 0 24 24" aria-hidden="true">
        <rect width="24" height="24" rx="4" fill="#7dc243"/>
        <rect x="8" y="4" width="8" height="5" fill="#fff"/>
        <rect x="5" y="9" width="14" height="8" rx="1" fill="#fff"/>
        <rect x="8" y="14" width="8" height="6" fill="#fff" stroke="#7dc243" stroke-width="1"/>
      </svg>
      <span>07 3952 1087</span>
    </div>
    <p class="email">dokoruwe@quorvel.net.au</p>
    <p class="address">3/412 Brackwin Rd Kelvinmoor QLD 4119<br>PO Box 829 Kelvinmoor QLD 4119</p>
    <div class="web-band">www.quorvel.net.au</div>
  </section>

  <section class="card card-back">
    <div class="brand-lockup">
      <span class="brand-dot"></span>
      <span class="brand-name">Quorvel</span>
    </div>
    <p class="tagline">CLEAR. SOUND. AHEAD.</p>
    <p class="services">Accountants<span class="sep">|</span>Tax Agents<span class="sep">|</span>Mortgage Brokers</p>
  </section>
</body>
</html>
```